Bed Company needs business card

Hello, we are a bed company that makes specialized magnets for beds. We are an alternative healing company. I need a modern and upscale business card. Please incorporate my logo for the card.

Accepted file formats are AI, EPS, and Press-Ready PDFS.

Please include all fonts or convert them to outlines regardless of file type.

If you are designing the card in Photoshop the file Must be 1200dpi.

I am open to anything for the business card.  I really like all of your designs and if you want to change the color of the logo, you can.  I will be making the final selection by Friday.  Thank You for all of your designs.  Feel Free to submit different color logos if you want.  

Reason: I will make a decision Final on Friday April 20th. 2012. Good Luck and Thank you all for the designs.

Target Market(s)

My target Market is people, who are looking for alternative healing.

Industry/Entity Type

Business

Requirements
Must have
• My logo must be incorporated. The front card must have

Name
Job Title

Address
Work
Cell
Fax
email
web

Just put in fake info for the card.

The back of the card. I want the logo on the back with color. I just want it to look modern and cool.

```html
<!DOCTYPE html>
<html lang="en">
<head>
<meta charset="utf-8">
<title>Lodestone Rest – Business Card</title>
<link rel="stylesheet" href="https://fonts.googleapis.com/css2?family=Caladea:wght@400;700&family=Open+Sans:wght@400;600&display=swap">
<style>
  :root {
    --green-deep: #1f6d0c;
    --green-brand: #238012;
    --ink: #111a05;
    --bg-top: #d9cf88;
    --bg-mid: #cfca86;
    --bg-low: #e4f5a6;
    --bg-bottom: #d6f2ad;
    --frame: #3c3a12;
  }
  * { margin: 0; padding: 0; box-sizing: border-box; }
  html, body { width: 1200px; height: 783px; overflow: hidden; }
  body {
    position: relative;
    background:
      repeating-linear-gradient(180deg, rgba(255,255,255,0.10) 0 6px, rgba(120,110,30,0.06) 6px 14px, rgba(255,255,255,0) 14px 22px),
      linear-gradient(180deg, var(--bg-top) 0%, var(--bg-mid) 28%, #dcd98f 48%, var(--bg-low) 62%, #eefbd0 72%, var(--bg-bottom) 88%, #e3f5b8 100%);
    font-family: "Caladea", Georgia, serif;
  }
  .card-frame {
    position: absolute;
    left: 42px; top: 42px;
    width: 1117px; height: 696px;
    border: 2px solid var(--frame);
    border-radius: 40px;
    box-shadow: inset 0 0 0 1px rgba(255,255,255,0.4);
  }
  .brand {
    position: absolute;
    left: 180px; top: 140px;
    display: flex; align-items: center; gap: 26px;
  }
  .brand-square {
    width: 96px; height: 96px;
    background: var(--green-brand);
  }
  .brand-name {
    font-family: "Caladea", Georgia, serif;
    font-weight: 700;
    font-size: 92px;
    line-height: 1;
    color: var(--green-brand);
    letter-spacing: -1px;
  }
  .brand-tagline {
    position: absolute;
    left: 563px; top: 262px;
    font-family: "Open Sans", Arial, sans-serif;
    font-size: 30px;
    letter-spacing: 3px;
    color: var(--green-deep);
  }
  .person {
    position: absolute;
    left: 0; width: 1254px; top: 326px;
    text-align: center;
    font-family: "Open Sans", Arial, sans-serif;
  }
  .person-name {
    font-size: 80px; line-height: 1;
    color: var(--green-deep);
    letter-spacing: -4px;
  }
  .person-title {
    margin-top: 14px;
    font-size: 38px; line-height: 1;
    color: var(--ink);
    letter-spacing: -1.5px;
  }
  .contact { position: absolute; color: var(--green-deep); line-height: 1; letter-spacing: -1.5px; }
  .contact-left { left: 134px; top: 556px; }
  .contact-right { left: 636px; top: 566px; }
  .city { font-size: 56px; letter-spacing: -3px; }
  .phone { margin-top: 12px; font-size: 44px; }
  .cell { margin-left: 126px; font-size: 54px; }
  .email { margin-top: 16px; font-size: 38px; }
</style>
</head>
<body>
  <div class="card-frame"></div>

  <div class="brand">
    <span class="brand-square"></span>
    <span class="brand-name">Lodestone Rest</span>
  </div>
  <div class="brand-tagline">Alternative Healing</div>

  <div class="person">
    <div class="person-name">Daniel Marsh</div>
    <div class="person-title">Business Manager</div>
  </div>

  <div class="contact contact-left">
    <div class="city">Boston</div>
    <div class="phone">phone: 54321</div>
  </div>

  <div class="contact contact-right">
    <div class="cell">Cell: 09876</div>
    <div class="email">Email:hello@lodestonerest.com</div>
  </div>
</body>
</html>
```